Use new branding for Orvel website

Orvel is a medical supplier of fitted socks for patients. Unlike a regular sock you receive upon admission that is slippery and prone to falling, Orvel unique factor is it’s gripping material which gives one traction while walking.
We would like to incorporate the new logo and branding into the Orvel website. The copy should stay the same. The logos in various formats and brand guidelines are included in the attachments. While the logos have a black or white background, you may use other colors if it integrates well with your design. Please submit your designs in either Wix or Squarespace
Hello all - additional information. We would like the design submission in either Wix or Squarespace.
Number of Pages Required
1 page

```html
<!DOCTYPE html>
<html lang="en">
<head>
<meta charset="utf-8">
<title>Orvel Tech – Compression Socks</title>
<link href="https://fonts.googleapis.com/css2?family=Roboto:wght@300;400;500;700&display=swap" rel="stylesheet">
<style>
:root{
  --yellow:#fbc116;
  --black:#111111;
  --text:#333333;
  --muted:#666666;
  --light:#f3f3f3;
  --line:#e2e2e2;
  --green:#6fae9a;
  --white:#ffffff;
}
*{box-sizing:border-box;margin:0;padding:0}
html,body{width:1200px;height:4890px;overflow:hidden}
body{position:relative;font-family:'Roboto',Arial,sans-serif;color:var(--text);background:var(--white)}
.abs{position:absolute}
.btn{position:absolute;background:var(--yellow);color:var(--white);font-size:14px;font-weight:500;text-transform:uppercase;display:flex;align-items:center;justify-content:center;letter-spacing:.3px}
.section-title{position:absolute;left:0;width:1200px;text-align:center;font-size:38px;font-weight:300;color:var(--black);text-transform:uppercase}
.section-title b{font-weight:500}

/* top bar */
.topbar{left:0;top:0;width:1200px;height:38px;background:var(--black);color:var(--white);font-size:12px}
.topbar .contact{left:100px;top:11px;display:flex;gap:8px;align-items:center}
.social{display:flex;gap:9px}
.social span{width:26px;height:26px;border:1.5px solid var(--white);border-radius:50%;display:block}
.topbar .social{right:100px;top:6px;position:absolute}

/* header */
.header{left:0;top:38px;width:1200px;height:72px;background:var(--white)}
.brand{font-size:36px;font-weight:400;letter-spacing:1px;color:var(--black);display:flex;align-items:center;gap:10px}
.brand i{width:22px;height:22px;border:3px solid var(--yellow);display:block}
.header .brand{left:100px;top:14px;position:absolute}
.nav{left:427px;top:29px;display:flex;font-size:14px;font-weight:500;color:var(--black)}
.nav a{color:inherit;text-decoration:none;margin-right:43px}

/* hero */
.hero{left:0;top:110px;width:1200px;height:588px;overflow:hidden;
  background:
    radial-gradient(ellipse 340px 420px at 830px 300px,rgba(226,86,40,.35),rgba(226,86,40,0) 70%),
    linear-gradient(180deg,#d4dde2 0%,#b9c6cd 22%,#8fa0a6 34%,#6f8a5a 46%,#55743a 62%,#3f5a2b 76%,#8f9598 86%,#a8acae 100%)}
.hero h1{left:100px;top:150px;font-size:40px;font-weight:400;line-height:49px;color:var(--black);text-transform:uppercase;position:absolute}
.hero .arrow{position:absolute;top:282px}
.dots{left:560px;top:545px;display:flex;gap:10px;position:absolute}
.dots span{width:11px;height:11px;border:1.5px solid var(--white);border-radius:50%}
.dots span.on{background:var(--white)}

/* about */
.about-title{left:641px;top:828px;font-size:38px;font-weight:300;color:var(--black)}
.about-title b{font-weight:500}
.about-copy{left:641px;top:890px;width:430px;font-size:12.5px;line-height:24px;color:#444}

/* styles */
.styles{left:0;top:1320px;width:1200px;height:610px;background:var(--light)}
.style-card{position:absolute;top:145px;width:318px;height:347px}
.style-label{position:absolute;top:513px;width:318px;text-align:center;font-size:17px;color:var(--black)}

/* benefits */
.benefit{position:absolute;font-size:13px;font-weight:700;color:var(--black)}
.benefit small{display:block;font-size:11px;font-weight:400;color:#444;margin-top:8px;line-height:17px}

/* news */
.news-card{position:absolute;top:2800px;width:320px;height:402px;background:var(--white);box-shadow:0 0 12px rgba(0,0,0,.1)}
.news-card .photo{position:absolute;left:8px;top:8px;width:304px;height:205px}
.news-card .date{position:absolute;left:78px;top:200px;width:146px;height:30px;background:var(--yellow);color:var(--white);font-size:12px;display:flex;align-items:center;justify-content:center;gap:6px}
.news-card h3{position:absolute;left:10px;top:250px;width:292px;font-size:16.5px;font-weight:700;line-height:21px;color:var(--black)}
.news-card p{position:absolute;left:10px;top:300px;width:300px;font-size:11.5px;line-height:20px;color:#666}
.news-card .more{position:absolute;left:10px;top:368px;font-size:11.5px;font-weight:700;color:var(--black)}

/* contact */
.contact-band{left:0;top:3340px;width:1200px;height:595px;background:var(--light)}
.contact-title{left:645px;top:3400px;font-size:34px;font-weight:300;line-height:41px;color:var(--black)}
.contact-title b{font-weight:500}
.contact-copy{left:645px;top:3490px;width:470px;font-size:12px;line-height:23px;color:#444}
.field{position:absolute;left:645px;width:468px;background:var(--white);border:1px solid var(--line);font-size:12px;color:#777;padding:16px}

/* faq */
.faq{position:absolute;width:462px;height:56px;border:1px solid var(--line);background:var(--white);display:flex;align-items:center;justify-content:space-between;padding:0 18px;font-size:14px;color:var(--black)}
.faq i{width:17px;height:17px;background:var(--black);border-radius:3px;position:relative;display:block}
.faq i::before,.faq i::after{content:"";position:absolute;background:var(--white);left:4px;top:7.5px;width:9px;height:2px}
.faq i::after{transform:rotate(90deg)}

/* footer */
.footer{left:0;top:4503px;width:1200px;height:387px;background:var(--black);color:var(--white)}
.footer h4{position:absolute;top:82px;font-size:17px;font-weight:500;text-transform:uppercase}
.footer .links{position:absolute;top:122px;font-size:13px;line-height:35px}
.footer .info{position:absolute;font-size:13px;line-height:21px}
.footer .pin{position:absolute;width:26px;height:26px;border:1.5px solid var(--white);border-radius:50%}
.footer .rule{position:absolute;left:85px;top:330px;width:1015px;height:1px;background:#444}
.footer .copy{position:absolute;left:0;top:352px;width:1200px;text-align:center;font-size:13px}
.newsletter{position:absolute;left:798px;top:158px;width:300px;height:52px;background:var(--white);border-radius:26px 0 0 26px;font-size:13px;color:#777;padding:16px 22px}
.newsletter .go{position:absolute;right:0;top:0;width:52px;height:52px;background:var(--yellow);display:flex;align-items:center;justify-content:center;border-radius:0 26px 26px 0}
</style>
</head>
<body>

<!-- top bar -->
<div class="abs topbar">
  <div class="abs contact">
    <svg width="12" height="12" viewBox="0 0 24 24"><path fill="#fff" d="M6.6 10.8a15 15 0 0 0 6.6 6.6l2.2-2.2a1 1 0 0 1 1-.25 11 11 0 0 0 3.6.6 1 1 0 0 1 1 1V20a1 1 0 0 1-1 1A17 17 0 0 1 3 4a1 1 0 0 1 1-1h3.5a1 1 0 0 1 1 1c0 1.25.2 2.45.6 3.6a1 1 0 0 1-.25 1z"/></svg>
    <span>(555) 214-0390</span><span>|</span>
    <svg width="12" height="10" viewBox="0 0 24 18"><rect x="1" y="1" width="22" height="16" fill="none" stroke="#fff" stroke-width="2"/><path d="M1 1l11 9 11-9" fill="none" stroke="#fff" stroke-width="2"/></svg>
    <span>hello@orvelsocks.com</span>
  </div>
  <div class="social"><span></span><span></span><span></span><span></span></div>
</div>

<!-- header -->
<div class="abs header">
  <div class="brand"><i></i>ORVEL</div>
  <nav class="abs nav"><a>HOME</a><a>PRODUCT</a><a>ABOUT US</a><a>BLOG</a><a>CONTACT US</a></nav>
  <div class="btn" style="left:1010px;top:17px;width:90px;height:40px;font-size:13px">Get a Quote</div>
</div>

<!-- hero -->
<div class="abs hero" role="img" aria-label="Runner in compression socks on a mountain road">
  <h1>The compression<br>socks that keep you<br>feeling fit and healthy</h1>
  <div class="btn" style="left:100px;top:320px;width:146px;height:40px">Get Started</div>
  <svg class="arrow" style="left:58px" width="16" height="34" viewBox="0 0 16 34"><path d="M14 2L2 17l12 15" fill="none" stroke="#fff" stroke-width="2"/></svg>
  <svg class="arrow" style="left:1120px" width="16" height="34" viewBox="0 0 16 34"><path d="M2 2l12 15L2 32" fill="none" stroke="#fff" stroke-width="2"/></svg>
  <div class="dots"><span></span><span class="on"></span><span></span><span></span></div>
</div>

<!-- about -->
<svg class="abs" style="left:125px;top:765px" width="415" height="478" viewBox="0 0 415 478">
  <defs>
    <linearGradient id="trail" x1="0" y1="0" x2="1" y2="1">
      <stop offset="0" stop-color="#d8c9a8"/>
      <stop offset=".45" stop-color="#a59a8a"/>
      <stop offset=".75" stop-color="#c7ad5a"/>
      <stop offset="1" stop-color="#6c6458"/>
    </linearGradient>
  </defs>
  <polygon points="207,4 411,121 411,357 207,474 4,357 4,121" fill="#fbc116"/>
  <polygon points="207,14 402,127 402,351 207,464 13,351 13,127" fill="url(#trail)" role="img" aria-label="Runner's leg in a compression sleeve on rocky trail"/>
</svg>
<h2 class="abs about-title">ABOUT <b>ORVEL TECH</b></h2>
<p class="abs about-copy">Lorem ipsum dolor sit amet, consectetur adipiscing elit, sed do eod tempor incididunt ut labore et dolore magna aliqua. Quis im suspenditrices gravida. Risus commodo viverra maecenas accumsan lacus l facilisis. Lorem ipsum dolor sit amet, consectetur adipiscing elit, sed do eod tempor incididunt ut labore et dolore magna aliqua. Quis im suspendtrigravida. Risus commodo viverra maecenas accumsan lacus vel facilisis. Lorem ipsum dolor sit amet, consectetur adipiscing elit, sed do eod tempor int ut labore et dolore magna aliqua. Quis im suspendtrices gravida. Risus commodo viverra maecenas accumsan lacus vel facilisis.</p>
<div class="btn" style="left:641px;top:1129px;width:146px;height:42px">Learn More</div>

<!-- styles -->
<section class="abs styles">
  <h2 class="section-title" style="top:70px">DIFFERENT <b>STYLES</b></h2>
  <div class="style-card" style="left:100px;background:radial-gradient(ellipse 90px 150px at 50% 52%,#ecd3a4,rgba(236,211,164,0) 100%),#fff" role="img" aria-label="Closed-toe beige compression stockings"></div>
  <div class="style-card" style="left:440px;background:radial-gradient(ellipse 85px 150px at 52% 48%,#3a3a3a,rgba(58,58,58,0) 100%),#fff" role="img" aria-label="Open-toe black compression stockings"></div>
  <div class="style-card" style="left:778px;background:radial-gradient(ellipse 95px 130px at 55% 48%,#8d8d8d,rgba(141,141,141,0) 100%),radial-gradient(ellipse 80px 50px at 45% 85%,#c99a7c,rgba(201,154,124,0) 100%),#fff" role="img" aria-label="Grey compression calf sleeves"></div>
  <div class="style-label" style="left:100px">CLOSED-TOE</div>
  <div class="style-label" style="left:440px">OPEN-TOE</div>
  <div class="style-label" style="left:778px">SLEEVES</div>
</section>

<!-- benefits -->
<h2 class="section-title" style="top:2025px">ORVEL <b>BENEFITS</b></h2>
<svg class="abs" style="left:0;top:2080px" width="1200" height="600" viewBox="0 2080 1200 600">
  <defs>
    <radialGradient id="glow" cx="50%" cy="50%" r="50%">
      <stop offset="0" stop-color="#fbc116" stop-opacity=".55"/>
      <stop offset=".7" stop-color="#fbc116" stop-opacity=".3"/>
      <stop offset="1" stop-color="#fbc116" stop-opacity=".12"/>
    </radialGradient>
    <radialGradient id="sock" cx="50%" cy="50%" r="50%">
      <stop offset="0" stop-color="#b88f6c" stop-opacity=".85"/>
      <stop offset=".6" stop-color="#c9a27f" stop-opacity=".5"/>
      <stop offset="1" stop-color="#d9b892" stop-opacity="0"/>
    </radialGradient>
  </defs>
  <circle cx="600" cy="2365" r="253" fill="none" stroke="#d8d8d8" stroke-width="1.5" stroke-dasharray="4 4"/>
  <circle cx="600" cy="2365" r="218" fill="url(#glow)"/>
  <ellipse cx="580" cy="2390" rx="120" ry="240" fill="url(#sock)" role="img" aria-label="Leg wearing beige knee-high compression sock"/>
  <g fill="none" stroke="#6fae9a" stroke-width="1.5">
    <polyline points="300,2200 395,2263 518,2263"/>
    <polyline points="240,2340 330,2457 545,2462"/>
    <polyline points="335,2530 475,2530 545,2505"/>
    <polyline points="375,2610 558,2558"/>
    <polyline points="666,2207 790,2207 875,2165"/>
    <polyline points="592,2349 880,2320"/>
    <polyline points="611,2518 735,2518 855,2470"/>
    <polyline points="643,2598 790,2590"/>
  </g>
  <g fill="#fff" stroke="#6fae9a" stroke-width="2">
    <circle cx="518" cy="2263" r="5"/><circle cx="545" cy="2461" r="5"/><circle cx="545" cy="2505" r="5"/>
    <circle cx="558" cy="2558" r="5"/><circle cx="666" cy="2207" r="5"/><circle cx="592" cy="2349" r="5"/>
    <circle cx="611" cy="2518" r="5"/><circle cx="643" cy="2598" r="5"/>
  </g>
</svg>
<div class="benefit" style="left:150px;top:2152px">20-30mmHg Graduated<br>Compression<small style="margin-top:4px">Medical Grade Compression to<br>Swelling Now</small></div>
<div class="benefit" style="left:137px;top:2310px">Ankle Protection<small>Stop Ankle Swelling/pain</small></div>
<div class="benefit" style="left:222px;top:2506px">Reinforced Heel<small>Cushion Every Step</small></div>
<div class="benefit" style="left:275px;top:2593px">Arch Support<small>Reduce Plantar Fasciitis</small></div>
<div class="benefit" style="left:880px;top:2152px">No Slip Cuff<small>Your Sock Won't Fall Down</small></div>
<div class="benefit" style="left:890px;top:2310px">Sturdy Fabric<small>No More Wimpy Thin Compression<br>&nbsp;&nbsp;&nbsp;Socks</small></div>
<div class="benefit" style="left:862px;top:2458px">Moisture Wicking Fabric<small>No More "Swamp Feet"</small></div>
<div class="benefit" style="left:793px;top:2593px">Reinforced Toe<small>prevent Blisters</small></div>

<!-- news -->
<h2 class="section-title" style="top:2718px">LATEST <b>NEWS</b></h2>
<article class="news-card" style="left:100px">
  <div class="photo" style="background:radial-gradient(ellipse 120px 80px at 55% 40%,#e3c3ad,rgba(227,195,173,0) 100%),linear-gradient(90deg,#eceae8 0%,#dcdfe6 55%,#3c5c98 100%)" role="img" aria-label="Doctor examining a patient's leg"></div>
  <div class="date"><svg width="11" height="11" viewBox="0 0 12 12"><rect x="1" y="2" width="10" height="9" fill="none" stroke="#fff" stroke-width="1.4"/><path d="M1 5h10" stroke="#fff" stroke-width="1.4"/></svg>JUNE 04,2021</div>
  <h3>Section 1.10.32 of "de Finibus Bonor um et Malorum"</h3>
  <p>Sed ut perspiciatis unde omnis iste natus error sit voluptatem accusantium doloremque laudantium, totam rem aperiam</p>
  <div class="more">READ MORE ▸</div>
</article>
<article class="news-card" style="left:440px">
  <div class="photo" style="background:radial-gradient(ellipse 90px 110px at 55% 55%,#f6f6f4,rgba(246,246,244,0) 100%),linear-gradient(90deg,#b79468 0%,#d8c4a6 45%,#e6e2dc 100%)" role="img" aria-label="Leg with white bandage and compression wrap"></div>
  <div class="date"><svg width="11" height="11" viewBox="0 0 12 12"><rect x="1" y="2" width="10" height="9" fill="none" stroke="#fff" stroke-width="1.4"/><path d="M1 5h10" stroke="#fff" stroke-width="1.4"/></svg>JUNE 04,2021</div>
  <h3>Section 1.10.32 of "de Finibus Bonor um et Malorum"</h3>
  <p>Sed ut perspiciatis unde omnis iste natus error sit voluptatem accusantium doloremque laudantium, totam rem aperiam</p>
  <div class="more">READ MORE ▸</div>
</article>
<article class="news-card" style="left:780px">
  <div class="photo" style="background:radial-gradient(ellipse 70px 60px at 72% 70%,#f0893f,rgba(240,137,63,0) 100%),linear-gradient(180deg,#5f7d55 0%,#4b6a42 45%,#7b7e7c 75%,#6a6c6b 100%)" role="img" aria-label="Runner wearing orange compression socks"></div>
  <div class="date"><svg width="11" height="11" viewBox="0 0 12 12"><rect x="1" y="2" width="10" height="9" fill="none" stroke="#fff" stroke-width="1.4"/><path d="M1 5h10" stroke="#fff" stroke-width="1.4"/></svg>JUNE 04,2021</div>
  <h3>Section 1.10.32 of "de Finibus Bonor um et Malorum"</h3>
  <p>Sed ut perspiciatis unde omnis iste natus error sit voluptatem accusantium doloremque laudantium, totam rem aperiam</p>
  <div class="more">READ MORE ▸</div>
</article>

<!-- contact -->
<div class="abs contact-band"></div>
<div class="abs" style="left:82px;top:3295px;width:478px;height:630px;background:var(--yellow)"></div>
<div class="abs" style="left:95px;top:3307px;width:477px;height:623px;background:radial-gradient(ellipse 160px 300px at 45% 55%,#c9a284,rgba(201,162,132,0) 100%),radial-gradient(ellipse 110px 160px at 88% 25%,#f5f5f7,rgba(245,245,247,0) 100%),linear-gradient(180deg,#e4ddd6 0%,#d4c8bd 60%,#bdb4ab 85%,#a89e95 100%)" role="img" aria-label="Woman seated putting on an open-toe compression stocking"></div>
<h2 class="abs contact-title">GET ALL TYPES OF<br><b>MEDICAL SOCKS FROM US</b></h2>
<p class="abs contact-copy">Lorem ipsum dolor sit amet, consectetur adipiscing elit, sed do eiusmpor incididunt ut labore et dolore magna aliqua. Quis ipsum suspendisse ultrices gravida. Risus commodo viverra maecenas accumsan lacus vel facilisis.</p>
<div class="field" style="top:3590px;height:50px">Your Name*</div>
<div class="field" style="top:3652px;height:50px">Your Email*</div>
<div class="field" style="top:3714px;height:92px">Your Message</div>
<div class="btn" style="left:645px;top:3822px;width:146px;height:38px">Submit</div>

<!-- faq -->
<h2 class="section-title" style="top:4018px">COMMONLY <b>ASKED QUESTIONS</b></h2>
<div class="faq" style="left:125px;top:4095px">Lorem ipsum dolor sit amet, consectetur adipiscing<i></i></div>
<div class="faq" style="left:612px;top:4095px">Lorem ipsum dolor sit amet, consectetur adipiscing<i></i></div>
<div class="faq" style="left:125px;top:4159px">Lorem ipsum dolor sit amet, consectetur adipiscing<i></i></div>
<div class="faq" style="left:612px;top:4159px">Lorem ipsum dolor sit amet, consectetur adipiscing<i></i></div>
<div class="faq" style="left:125px;top:4223px">Lorem ipsum dolor sit amet, consectetur adipiscing<i></i></div>
<div class="faq" style="left:612px;top:4223px">Lorem ipsum dolor sit amet, consectetur adipiscing<i></i></div>
<div class="faq" style="left:125px;top:4287px">Lorem ipsum dolor sit amet, consectetur adipiscing<i></i></div>
<div class="faq" style="left:612px;top:4287px">Lorem ipsum dolor sit amet, consectetur adipiscing<i></i></div>
<div class="faq" style="left:125px;top:4351px">Lorem ipsum dolor sit amet, consectetur adipiscing<i></i></div>
<div class="faq" style="left:612px;top:4351px">Lorem ipsum dolor sit amet, consectetur adipiscing<i></i></div>

<!-- footer -->
<footer class="abs footer">
  <div class="brand abs" style="left:100px;top:80px;color:var(--white)"><i></i>ORVEL</div>
  <div class="social abs" style="left:110px;top:150px"><span style="width:34px;height:34px"></span><span style="width:34px;height:34px"></span><span style="width:34px;height:34px"></span><span style="width:34px;height:34px"></span></div>

  <h4 style="left:348px">Quick Link</h4>
  <div class="links" style="left:348px">Home<br>Product<br>About Us<br>Blog<br>Contact Us</div>

  <h4 style="left:521px">Contact Us</h4>
  <div class="pin" style="left:521px;top:122px"></div>
  <div class="info" style="left:553px;top:120px">123 Your Adress Goes Here.<br>CA, 1234567</div>
  <div class="pin" style="left:521px;top:176px"></div>
  <div class="info" style="left:553px;top:174px">Phone:<br>(555) 555 0142</div>
  <div class="pin" style="left:521px;top:230px"></div>
  <div class="info" style="left:553px;top:228px">Email:<br>hello@orveltech.com</div>

  <h4 style="left:805px">Our Newsletter</h4>
  <div class="info" style="left:805px;top:120px">Sign up to stay in the Pest Solutions</div>
  <div class="newsletter">Enter Email
    <div class="go"><svg width="20" height="20" viewBox="0 0 24 24"><path d="M2 12L22 3l-6 19-4-8z" fill="#fff"/></svg></div>
  </div>

  <div class="rule"></div>
  <div class="copy">Copyright © 2021 Orvel Tech. All rights</div>
</footer>

</body>
</html>
```